Home and body fragrance business needs a candle box design

We need a box design for our new line of luxury candles. Our products are tropical island inspired. In addition to the box, a matching label for the candle jar is required. Our logo, candle jar and lid are attached. We will be using an autolock box. Box template and sample photo are attached. The design should communicate reconnecting, reviving and relaxing at luxury island retreat.

Box Dimension = L= 3 inches W=3 inches H=3.725 inches

Box Front Text = "pure soy wax candle"; "Velmarine"(aroma name); "breath relax find you"(tagline)

Box Other Text = "HAND POURED. EACH CANDLE IS CLEAN BURNING, WITH A PURE COTTON WICK AND IS INFUSED WITH A HINT OF THE FINEST FRAGRANCE OF PARADISE"

Box Bottom Text = . Estimated burn time 75 hours. Net wt 370 g.

Jar label text = logo, and aroma name
Updates

Reason: I have increased the design budget in an effort to attack more design submissions.

Target Market(s)

Women 25 - 55

Industry/Entity Type

Business

Font styles to use
Serif
Script

Colors

Designer to choose colors to be used in the design.

Requirements
Must have
• Gold. Colours reminiscent of an Elegant LUXURY tropical island vacation. These candles will retail for $45 each, so an upscale design is essential.
Nice to have
• Designs that I like are: www.brindelmaroquest.com ; vorsanel.com; hapsilverdune.com;
Should not have
• Styles reminiscent of wasting away in tobrentwaldhay

```html
<!DOCTYPE html>
<html lang="en">
<head>
<meta charset="utf-8">
<title>Velmarine – Candle Box Panels</title>
<link rel="stylesheet" href="https://fonts.googleapis.com/css2?family=Open+Sans:wght@400;600&family=Advent+Pro:wght@300&display=swap">
<style>
  :root {
    --stage: #ededee;
    --slate: #2f3537;
    --slate-deep: #262b2d;
    --leaf-gold: #8a7650;
    --panel-gold-light: #c6ad7c;
    --panel-gold-dark: #ae9463;
    --frame-gold-a: #f3d98d;
    --frame-gold-b: #b2832d;
    --cream: #f4ecd9;
    --white: #ffffff;
  }
  * { margin: 0; padding: 0; box-sizing: border-box; }
  html, body { width: 1200px; height: 675px; overflow: hidden; background: var(--stage); }
  .canvas {
    position: relative; width: 1200px; height: 675px;
    display: flex; justify-content: center; align-items: center;
  }
  .box-panel {
    position: relative; width: 380px; height: 472px; overflow: hidden;
    background: var(--slate);
  }
  .box-panel + .box-panel { border-left: 1px solid #1f2426; }
  .leaf-artwork {
    position: absolute; inset: 0;
    background:
      radial-gradient(ellipse at 20% 30%, rgba(138,118,80,0.28), transparent 55%),
      radial-gradient(ellipse at 80% 70%, rgba(138,118,80,0.22), transparent 55%),
      linear-gradient(135deg, var(--slate) 0%, var(--slate-deep) 100%);
  }
  .side-copy {
    position: absolute; left: 22px; bottom: 60px; width: 130px;
    font-family: "Open Sans", sans-serif; font-size: 6.5px; line-height: 1.6;
    letter-spacing: 0.04em; color: var(--panel-gold-light);
  }
  .label-frame {
    position: absolute; top: 24px; bottom: 26px; left: 50px; right: 50px;
    padding: 5px;
    background: linear-gradient(160deg, var(--frame-gold-a), var(--frame-gold-b) 45%, var(--frame-gold-a) 70%, var(--frame-gold-b));
  }
  .label {
    position: relative; width: 100%; height: 100%;
    background: linear-gradient(180deg, var(--panel-gold-light), var(--panel-gold-dark));
    color: var(--white); text-align: center;
  }
  .house-name {
    position: absolute; top: 16px; left: 0; right: 0;
    font-family: "Open Sans", sans-serif; font-weight: 400; font-size: 14px;
    letter-spacing: 0.12em; text-transform: uppercase; color: var(--cream);
  }
  .aroma {
    position: absolute; top: 176px; left: 0; right: 0;
  }
  .aroma-name {
    font-family: "Open Sans", sans-serif; font-weight: 400; font-size: 34px;
    line-height: 1.1; color: var(--white);
  }
  .tagline {
    margin-top: 8px;
    font-family: "Open Sans", sans-serif; font-weight: 600; font-size: 9px;
    letter-spacing: 0.03em; color: var(--white);
  }
  .product-line {
    position: absolute; bottom: 14px; left: 0; right: 0;
  }
  .product-type {
    font-family: "Advent Pro", sans-serif; font-weight: 300; font-size: 21px;
    letter-spacing: 0.02em; color: var(--cream);
  }
  .product-facts {
    margin-top: 2px;
    font-family: "Open Sans", sans-serif; font-size: 8px; color: var(--white);
  }
</style>
</head>
<body>
  <main class="canvas">
    <section class="box-panel box-side">
      <div class="leaf-artwork" role="img" aria-label="Gold line illustration of tropical palm and banana leaves on dark slate"></div>
      <p class="side-copy">HAND POURED. EACH CANDLE IS CLEAN BURNING, WITH A PURE COTTON WICK AND IS INFUSED WITH A HINT OF THE FINEST FRAGRANCE OF PARADISE</p>
    </section>
    <section class="box-panel box-front">
      <div class="leaf-artwork" role="img" aria-label="Gold line illustration of tropical palm and banana leaves on dark slate"></div>
      <div class="label-frame">
        <div class="label">
          <p class="house-name">Isla Marenza</p>
          <div class="aroma">
            <h1 class="aroma-name">Velmarine</h1>
            <p class="tagline">BREATH RELAX FIND YOU</p>
          </div>
          <div class="product-line">
            <p class="product-type">PURE SOY WAX CANDLE</p>
            <p class="product-facts">Estimated burn time 75 hours. Net wt 370 g</p>
          </div>
        </div>
      </div>
    </section>
  </main>
</body>
</html>
```